Lumaform website scandinavian interior design

Existing website: http://lumaform-example.no/

Webdesign for interior designer Ragna Tvedtholm. The company name is Lumaform. Scandinavian interiør is known to be simple and elegant. The website will be in Norwegian, we are working on the text. The website needs to have a few more pages than just the front page. Here are the different titles of the pages:

1. Hjem
2. Om Lumaform
3. Tjenester og priser
4.. Kontakt oss

There should be Facebook and Instagram icons somewhere at the bottom of the website.

The logo we want to use is attached (pink with black print, see attachment )

We have attached images for inspiration. We want to use some of these colors. The color in the logo, The style should be elegant, modern and delicate.

It is imprtant that the website is user friendly.

Target Market(s)

People who want to decorate their home
Companies and public sector who need to redecorate

Industry/Entity Type

Interior Designer

Coding

Coded - Design and coding required

Number of Pages Required

5+ page

Font styles to use
Other font styles liked:
• see example in the logo breakdown

Requirements
Must have
• Elegant, modern and delicate design
Images of design, see examples attached
Colors similar to the pictures
Should not have
• Too bright colors
Pictures of people

```html
<!DOCTYPE html>
<html lang="no">
<head>
<meta charset="utf-8">
<title>Lumaform – Interiørdesign</title>
<link href="https://fonts.googleapis.com/css2?family=Playfair+Display:wght@400;700&family=Open+Sans:wght@400;600;700&display=swap" rel="stylesheet">
<style>
:root{
  --blush:#f0d5ce;
  --blush-soft:#f6e4df;
  --ink:#2b2523;
  --text:#5b5451;
  --muted:#8d8582;
  --cocoa:#3b1f1a;
  --line:#d9c3bd;
  --white:#ffffff;
  --paper:#f7f5f4;
}
*{margin:0;padding:0;box-sizing:border-box}
html,body{width:783px;height:1200px;overflow:hidden;background:var(--white)}
body{position:relative;font-family:"Open Sans",Arial,sans-serif;color:var(--text)}
.serif{font-family:"Playfair Display",Georgia,serif}

/* header */
.site-header{position:absolute;left:0;top:0;width:783px;height:100px;background:var(--paper)}
.brand-block{position:absolute;left:0;top:0;width:285px;height:100px;background:var(--blush);display:flex;align-items:center;justify-content:center;gap:8px}
.brand-mark{width:12px;height:12px;border:1.5px solid var(--ink)}
.brand-name{font-family:"Playfair Display",Georgia,serif;font-size:26px;font-weight:700;color:var(--ink)}
.contact-bar{position:absolute;right:40px;top:16px;display:flex;gap:28px;font-size:7.5px;color:var(--ink)}
.contact-bar span{display:flex;align-items:center;gap:5px}
.contact-bar svg{width:9px;height:9px}
.main-nav{position:absolute;left:420px;top:56px;display:flex;gap:0;font-size:7px;font-weight:600;letter-spacing:.6px}
.main-nav a{color:var(--ink);text-decoration:none;padding:6px 12px;border-left:1px solid var(--line)}
.main-nav a:first-child{border-left:none}

/* hero */
.hero{position:absolute;left:0;top:100px;width:783px;height:230px;background:linear-gradient(100deg,#d8cfc6 0%,#ece7e1 40%,#c9a57f 75%,#b88e66 100%)}
.hero-accent{position:absolute;left:0;top:300px;width:180px;height:65px;background:var(--blush)}
.hero-title{position:absolute;left:0;width:783px;top:172px;text-align:center;font-family:"Playfair Display",Georgia,serif;font-weight:700;font-size:17px;line-height:1.3;color:var(--ink)}
.btn{display:inline-block;background:var(--cocoa);color:var(--white);font-size:6px;font-weight:700;letter-spacing:.8px;padding:6px 14px;text-decoration:none}
.hero-btn{position:absolute;left:363px;top:226px}
.arrow{position:absolute;top:200px;width:22px;height:22px;border:1.5px solid var(--white);border-radius:50%}
.arrow svg{width:100%;height:100%}
.dots{position:absolute;top:308px;left:371px;display:flex;gap:5px}
.dots i{width:6px;height:6px;border-radius:50%;border:1px solid var(--white)}
.dots i.on{background:var(--white)}

/* about */
.about-frame{position:absolute;left:140px;top:392px;width:215px;height:200px;border:1px solid var(--blush)}
.about-photo{position:absolute;left:150px;top:382px;width:210px;height:200px;background:linear-gradient(160deg,#e9e6e2 0%,#cfc9c2 55%,#8a6b55 100%)}
.about-text{position:absolute;left:392px;top:385px;width:250px}
.about-text h2{font-family:"Playfair Display",Georgia,serif;font-size:22px;color:var(--ink);margin-bottom:12px}
.about-text p{font-size:6.5px;line-height:1.65;margin-bottom:8px}
.about-text strong{color:var(--ink)}

/* services */
.section-title{position:absolute;left:0;top:645px;width:783px;display:flex;justify-content:center;align-items:center;gap:12px}
.section-title h2{font-family:"Playfair Display",Georgia,serif;font-size:19px;color:var(--ink);font-weight:400}
.section-title span{width:60px;height:1px;background:var(--ink)}
.services{position:absolute;left:160px;top:690px;display:flex;gap:11px}
.card{width:146px;height:215px;background:var(--blush);position:relative;text-align:center}
.card-photo{position:absolute;left:10px;top:-8px;width:126px;height:78px}
.card h3{margin-top:82px;font-family:"Playfair Display",Georgia,serif;font-size:12px;color:var(--ink)}
.card p{font-size:6.5px;line-height:1.6;margin:8px 14px 14px;color:var(--ink)}
.divider{position:absolute;left:0;top:935px;width:783px;height:1px}

/* footer */
.site-footer{position:absolute;left:0;top:975px;width:783px;height:200px;background:var(--blush)}
.footer-links{position:absolute;left:150px;top:35px;list-style:none;font-size:7px;line-height:2.7;color:var(--ink)}
.footer-col-line{position:absolute;top:20px;width:1px;height:150px;background:var(--line)}
.footer-brand{position:absolute;left:290px;top:55px;width:200px;display:flex;justify-content:center;align-items:center;gap:7px}
.footer-brand .brand-name{font-size:22px}
.socials{position:absolute;left:362px;top:115px;display:flex;gap:10px}
.socials i{width:18px;height:18px;border-radius:50%;border:1.5px solid var(--ink)}
.footer-contact{position:absolute;left:520px;top:30px;font-size:6.8px;line-height:1.6;color:var(--ink)}
.footer-contact h4{font-size:7.5px;font-weight:700;margin-bottom:4px}
.footer-contact b{display:block;margin-top:7px}
.legal{position:absolute;left:0;top:1175px;width:783px;height:25px;display:flex;align-items:center;justify-content:center;font-size:6px;color:var(--muted)}
</style>
</head>
<body>

<header class="site-header">
  <div class="brand-block"><span class="brand-mark"></span><span class="brand-name">Lumaform</span></div>
  <div class="contact-bar">
    <span><svg viewBox="0 0 10 10"><path d="M2 1l2 2-1 1.3c.6 1.2 1.5 2.1 2.7 2.7L7 6l2 2-1.3 1.3C4.5 9 1 5.5.7 2.3z" fill="#2b2523"/></svg>+47 900 12 345<br>post@lumaform-example.no</span>
    <span><svg viewBox="0 0 10 10"><path d="M5 .5a3 3 0 0 0-3 3c0 2.3 3 6 3 6s3-3.7 3-6a3 3 0 0 0-3-3zm0 4.2a1.2 1.2 0 1 1 0-2.4 1.2 1.2 0 0 1 0 2.4z" fill="#2b2523"/></svg>Ring oss<br>+47 900 12 345</span>
  </div>
  <nav class="main-nav">
    <a href="#">HJEM</a><a href="#">OM LUMAFORM</a><a href="#">TJENESTER OG PRISER</a><a href="#">KONTAKT OSS</a>
  </nav>
</header>

<section class="hero" role="img" aria-label="Lyst spisestue med trebord, grå stoler og trapp i lyst tre"></section>
<div class="hero-accent"></div>
<h1 class="hero-title">Trenger du hjelp til utvikling<br>av interiørmiljøer?</h1>
<a class="btn hero-btn" href="#">KONTAKT OSS</a>
<span class="arrow" style="left:114px"><svg viewBox="0 0 22 22"><path d="M13 6l-5 5 5 5" stroke="#fff" stroke-width="1.5" fill="none"/></svg></span>
<span class="arrow" style="left:647px"><svg viewBox="0 0 22 22"><path d="M9 6l5 5-5 5" stroke="#fff" stroke-width="1.5" fill="none"/></svg></span>
<div class="dots"><i class="on"></i><i></i><i></i></div>

<div class="about-frame"></div>
<div class="about-photo" role="img" aria-label="Lys stue med hvit peis og sittegruppe"></div>
<section class="about-text">
  <h2>Om Lumaform</h2>
  <p>Ragna Tvedtholm er daglig leder og interiørarkitekt i Lumaform. Vi hjelper både private og bedrifter med å skape rom som er enkle, vakre og funksjonelle. Med bakgrunn i skandinavisk design legger vi vekt på lys, naturlige materialer og gode detaljer som varer over tid.</p>
  <p>Vi tar oppdrag i hele regionen og tilpasser hvert prosjekt etter dine behov, ønsker og budsjett.</p>
  <p><strong>Ragna T.</strong><br>Vårt mål er å gjøre prosessen trygg og oversiktlig. Fra første befaring til ferdig rom følger vi deg tett, med tydelige skisser, forslag til farger og møbler, og praktisk oppfølging.</p>
  <p>Ta gjerne kontakt for en uforpliktende samtale om ditt neste prosjekt, stort eller lite.</p>
  <p><strong>Ragna Tvedtholm – Interiørarkitekt</strong></p>
</section>

<div class="section-title"><span></span><h2>Tjenester</h2><span></span></div>
<section class="services">
  <article class="card">
    <div class="card-photo" role="img" aria-label="Planløsning sett ovenfra" style="background:linear-gradient(135deg,#e8ddd4,#a88c74)"></div>
    <h3>Planlegger</h3>
    <p>Vi lager gode planløsninger som utnytter rommet best mulig, med fokus på flyt og lys.</p>
    <a class="btn" href="#">LES MER</a>
  </article>
  <article class="card">
    <div class="card-photo" role="img" aria-label="Innredet stue med sofa og puter" style="background:linear-gradient(135deg,#efe9e3,#b9a595)"></div>
    <h3>Interiør</h3>
    <p>Helhetlig innredning med farger, møbler og tekstiler som gir et rolig og elegant uttrykk.</p>
    <a class="btn" href="#">LES MER</a>
  </article>
  <article class="card">
    <div class="card-photo" role="img" aria-label="Fargeprøver og tegninger på bord" style="background:linear-gradient(135deg,#f2ece6,#c4a48c)"></div>
    <h3>Rådgivning</h3>
    <p>Personlig rådgivning for hjem og næring, tilpasset dine behov og ditt budsjett.</p>
    <a class="btn" href="#">LES MER</a>
  </article>
</section>

<footer class="site-footer">
  <ul class="footer-links">
    <li>Hjem</li><li>Om Lumaform</li><li>Tjenester og priser</li><li>Kontakt oss</li>
  </ul>
  <span class="footer-col-line" style="left:270px"></span>
  <div class="footer-brand"><span class="brand-mark"></span><span class="brand-name">Lumaform</span></div>
  <div class="socials"><i></i><i></i></div>
  <span class="footer-col-line" style="left:505px"></span>
  <address class="footer-contact" style="font-style:normal">
    <h4>Post/besøksadresse</h4>
    Lumaform v/ Ragna Tvedtholm<br>Strandveien 14<br>3015 Drammen
    <b>Telefon</b>+47 900 12 345
    <b>E-post</b>post@lumaform-example.no
  </address>
</footer>
<div class="legal">© 2024 Lumaform. All rights reserved. &nbsp;|&nbsp; Privacy Policy</div>

</body>
</html>
```